Poster/Sign Design Project

I'm looking for someone to help to spruce up our sign that promotes all of the things that the Parent Teacher Association does for each grade. Please see the attachment for the content needed on the one page. We are looking to include the content in a compelling design that is clean, crisp, and easy to read.

```html
<!DOCTYPE html>
<html lang="en">
<head>
<meta charset="utf-8">
<title>Alder Creek PTA – Where Your Donation Goes</title>
<link href="https://fonts.googleapis.com/css2?family=Lato:ital,wght@0,400;0,700;0,900;1,400&display=swap" rel="stylesheet">
<style>
  :root {
    --red: #ea3a24;
    --green: #8cc43f;
    --ink: #1c1c1c;
    --white: #ffffff;
    --photo-a: #d9b48f;
    --photo-b: #6c8fbf;
  }
  * { box-sizing: border-box; margin: 0; padding: 0; }
  html, body { width: 868px; height: 1200px; overflow: hidden; background: var(--white); }
  body { font-family: "Lato", Arial, sans-serif; color: var(--ink); }
  .flyer { position: relative; width: 868px; height: 1200px; overflow: hidden; background: var(--white); }

  .hero-photo {
    position: absolute; left: 0; top: 0; width: 478px; height: 430px;
    background: linear-gradient(135deg, #f1e6d8 0%, var(--photo-a) 45%, var(--photo-b) 80%, #e4573f 100%);
  }
  .hero-panel {
    position: absolute; left: 478px; top: 0; width: 390px; height: 430px;
    background: var(--red); padding: 30px 8px 0 16px; overflow: hidden;
  }
  .hero-headline {
    font-weight: 400; font-size: 48px; line-height: 62px; letter-spacing: -2.5px;
    word-spacing: -4px; text-transform: uppercase; white-space: nowrap;
  }
  .hero-headline .dark { color: var(--ink); font-style: italic; }
  .hero-headline .light { color: var(--white); }

  .ribbon { position: absolute; left: 30px; top: 448px; width: 810px; height: 58px; }
  .ribbon svg { position: absolute; inset: 0; }
  .ribbon-text {
    position: absolute; inset: 0; display: flex; align-items: center; justify-content: center;
    color: var(--white); font-weight: 700; font-size: 33px; letter-spacing: 0.2px;
  }

  .columns { position: absolute; left: 40px; top: 522px; width: 800px; display: flex; justify-content: space-between; }
  .column { width: 250px; }
  .column.wide { width: 240px; }
  .pill {
    display: inline-block; background: var(--red); color: var(--white); font-weight: 700;
    font-size: 17px; line-height: 21px; padding: 9px 22px; border-radius: 24px; text-transform: uppercase;
  }
  .items { list-style: none; margin-top: 30px; font-weight: 700; font-size: 17px; line-height: 22px; }
  .items.tight { margin-top: 22px; }
  .items li { position: relative; padding-left: 16px; }
  .items li::before {
    content: ""; position: absolute; left: 0; top: 7px; width: 9px; height: 9px; border-radius: 50%; background: var(--green);
  }

  .kinder-heading {
    position: absolute; left: 0; top: 738px; width: 868px; text-align: center;
    color: var(--red); font-weight: 700; font-size: 40px; line-height: 46px;
  }
  .label { position: absolute; left: 298px; top: 836px; width: 272px; height: 34px; }
  .label svg { position: absolute; inset: 0; }
  .label-text {
    position: absolute; inset: 0; display: flex; align-items: center; justify-content: center;
    color: var(--white); font-weight: 700; font-size: 21px;
  }
  .kinder-list {
    position: absolute; left: 0; top: 872px; width: 868px; text-align: center;
    font-size: 21px; line-height: 29px; font-weight: 400;
  }

  .footer-wave { position: absolute; left: 0; top: 990px; width: 868px; height: 210px; }
  .school-art {
    position: absolute; left: 384px; top: 1098px; width: 100px; height: 84px; border-radius: 8px;
    background: linear-gradient(180deg, #cfe6f2 0%, #d8513e 60%, #7aa34a 100%);
  }
</style>
</head>
<body>
<main class="flyer">
  <div class="hero-photo" role="img" aria-label="Photo of a teacher and a young student painting at a colourful art table"></div>
  <section class="hero-panel">
    <h1 class="hero-headline">
      <span class="dark">Every Dollar<br>That You<br>Donate</span><span class="light"> To<br>The Alder<br>Creek PTA<br>Stays at Alder</span>
    </h1>
  </section>

  <div class="ribbon">
    <svg viewBox="0 0 810 58" preserveAspectRatio="none" aria-hidden="true">
      <polygon points="0,14 800,0 780,26 810,44 10,58 28,34" fill="var(--green)"/>
    </svg>
    <div class="ribbon-text">YOUR DONATIONS TO ALDER PTA PAY FOR:</div>
  </div>

  <section class="columns">
    <div class="column">
      <span class="pill">Basic Classroom<br>Supplies</span>
      <ul class="items">
        <li>pencils,</li>
        <li>pens,</li>
        <li>glue</li>
        <li>Recess Equipment</li>
      </ul>
    </div>
    <div class="column">
      <span class="pill">Office Supplies</span>
      <ul class="items tight">
        <li>ink cartridges,</li>
        <li>paper,</li>
        <li>toner</li>
        <li>Tablets &amp;</li>
        <li>laptops for students and teachers</li>
      </ul>
    </div>
    <div class="column wide">
      <span class="pill">Student Assemblies</span>
      <ul class="items tight">
        <li>Professional Development for Teachers Programs and Events such as: Book Fair, Family Science Night, Art Show, Variety Show and Spring Faire</li>
      </ul>
    </div>
  </section>

  <h2 class="kinder-heading">IN KINDERGARTEN PTA DONATIONS<br>ALSO PAY FOR:</h2>
  <div class="label">
    <svg viewBox="0 0 272 34" preserveAspectRatio="none" aria-hidden="true">
      <polygon points="0,8 272,0 260,17 270,32 4,34 16,21" fill="var(--green)"/>
    </svg>
    <div class="label-text">SCIENCE SPECIALIST</div>
  </div>
  <p class="kinder-list">
    Bayview Botanical Gardens<br>
    Leaf Hopper Hikes, Learn Quest Labs, June Halloway - Storyteller,<br>
    Classroom supplies - Art, Science,<br>
    Educational toys and games for choice learning<br>
    Grade level snack bags
  </p>

  <svg class="footer-wave" viewBox="0 0 868 210" aria-hidden="true">
    <path d="M0,40 C260,130 560,130 868,20 L868,210 L0,210 Z" fill="var(--green)"/>
    <path d="M0,62 C260,152 560,150 868,44 L868,210 L0,210 Z" fill="var(--red)"/>
    <path d="M0,210 C200,125 660,125 868,210 Z" fill="var(--green)"/>
    <path d="M10,210 C210,135 650,135 858,210 Z" fill="var(--white)"/>
  </svg>
  <div class="school-art" role="img" aria-label="Illustration of a red schoolhouse with trees"></div>
</main>
</body>
</html>
```